Q-Rolls Business Card

We are a modern retail clothing store. Established in 1994. I need a presentable card that will amaze vendors when given to them.

Front: Logo in middle
Info Side:

Name: Tomas Velder
Cell: 630-812-4463
Work: 630-917-3384 EXT. 417
Email: Tomas@q-rolls-example.com
Website: www.Q-rolls-example.com

Industry/Entity Type

Business

```html
<!DOCTYPE html>
<html lang="en">
<head>
<meta charset="utf-8">
<title>Q-Rolls Business Card</title>
<link rel="stylesheet" href="https://fonts.googleapis.com/css2?family=Montserrat:wght@300;400;700;800&display=swap">
<style>
  :root {
    --stage: #2a2522;
    --card-black: #050203;
    --card-glow: #5a1426;
    --brand-yellow: #f7b500;
    --text-light: #f1ece6;
    --shadow: rgba(0, 0, 0, 0.55);
  }
  * { box-sizing: border-box; margin: 0; padding: 0; }
  html, body {
    width: 1200px;
    height: 913px;
    overflow: hidden;
    background: var(--stage);
    font-family: "Montserrat", Arial, sans-serif;
  }
  .card-set {
    position: relative;
    width: 1200px;
    height: 913px;
    display: flex;
    align-items: center;
    justify-content: center;
    gap: 48px;
  }
  .card {
    position: relative;
    width: 540px;
    height: 309px;
    border-radius: 2px;
    background:
      radial-gradient(ellipse 55% 60% at 50% 45%, var(--card-glow) 0%, rgba(90, 20, 38, 0.35) 45%, var(--card-black) 80%),
      var(--card-black);
    box-shadow: 0 18px 40px var(--shadow);
    overflow: hidden;
  }
  .card--info {
    background:
      radial-gradient(ellipse 40% 55% at 53% 42%, var(--card-glow) 0%, rgba(90, 20, 38, 0.3) 50%, var(--card-black) 85%),
      var(--card-black);
  }
  .brand-name {
    color: var(--brand-yellow);
    font-weight: 800;
    letter-spacing: 1px;
    white-space: nowrap;
  }
  .card--front .brand-name {
    position: absolute;
    left: 50%;
    top: 50%;
    transform: translate(-50%, -50%);
    font-size: 76px;
  }
  .card--info .brand-name {
    position: absolute;
    left: 38px;
    top: 172px;
    font-size: 46px;
  }
  .divider {
    position: absolute;
    left: 268px;
    top: 58px;
    width: 2px;
    height: 160px;
    background: var(--brand-yellow);
  }
  .contact {
    position: absolute;
    left: 290px;
    top: 64px;
    right: 12px;
  }
  .contact-name {
    color: var(--brand-yellow);
    font-weight: 700;
    font-size: 17px;
    margin-bottom: 6px;
  }
  .contact-list { list-style: none; }
  .contact-item {
    display: flex;
    align-items: center;
    gap: 7px;
    color: var(--text-light);
    font-weight: 300;
    font-size: 12.5px;
    line-height: 22px;
    white-space: nowrap;
  }
  .contact-icon {
    width: 11px;
    height: 11px;
    flex: none;
    fill: none;
    stroke: var(--brand-yellow);
    stroke-width: 1.4;
  }
</style>
</head>
<body>
  <main class="card-set">
    <section class="card card--front" aria-label="Card front">
      <span class="brand-name">Q-Rolls</span>
    </section>

    <section class="card card--info" aria-label="Card back">
      <span class="brand-name">Q-Rolls</span>
      <div class="divider"></div>
      <div class="contact">
        <p class="contact-name">Tomas Velder</p>
        <ul class="contact-list">
          <li class="contact-item">
            <svg class="contact-icon" viewBox="0 0 12 12"><rect x="3" y="1" width="6" height="10" rx="1"/><line x1="5" y1="9" x2="7" y2="9"/></svg>
            630-812-4463
          </li>
          <li class="contact-item">
            <svg class="contact-icon" viewBox="0 0 12 12"><circle cx="6" cy="6" r="5"/><path d="M4 3.5 l1 1.5 -0.7 0.7 q1 1.6 2 2 l0.7-0.7 1.5 1"/></svg>
            630-917-3384 EXT. 417
          </li>
          <li class="contact-item">
            <svg class="contact-icon" viewBox="0 0 12 12"><rect x="1" y="2.5" width="10" height="7"/><path d="M1 2.5 L6 6.5 L11 2.5"/></svg>
            Tomas@q-rolls-example.com
          </li>
          <li class="contact-item">
            <svg class="contact-icon" viewBox="0 0 12 12"><circle cx="6" cy="6" r="5"/><ellipse cx="6" cy="6" rx="2.2" ry="5"/><line x1="1" y1="6" x2="11" y2="6"/></svg>
            www.Q-rolls-example.com
          </li>
        </ul>
      </div>
    </section>
  </main>
</body>
</html>
```